Business card for Internet Marketing Consultant

Simple - need a nice business card design using the logo elements and colors. Keywords: Progressive, professional, stylish, minimalist. Please use the kr as part of the design.

Info for card:

Gareth Pennock
Internet Marketing Strategist
Phone: (555) 813-2064
Email: gareth@korvantareach.com
Address: 2156 N. Halvern Ave., Ste. 118
Tucson, Arizona 85710

Website: www.korvantareach.com

Business

Sans Serif

```html
<!DOCTYPE html>
<html lang="en">
<head>
<meta charset="utf-8">
<title>Gareth Pennock – Business Card</title>
<link rel="stylesheet" href="https://fonts.googleapis.com/css2?family=Arimo:wght@400;700&family=Roboto+Condensed:wght@400;700&display=swap">
<style>
  :root {
    --paper: #ffffff;
    --trim: #6fe6ee;
    --name-blue: #1a2aa8;
    --brand-blue: #2f6bf4;
    --brand-green: #66f542;
    --tagline: #4a4a7a;
    --rule: #3a24c4;
    --ink: #111111;
  }
  html, body {
    margin: 0;
    padding: 0;
    width: 1200px;
    height: 735px;
    overflow: hidden;
    background: var(--paper);
  }
  .card {
    position: relative;
    width: 1200px;
    height: 735px;
    background: var(--paper);
  }
  .trim-line {
    position: absolute;
    left: 44px;
    top: 44px;
    width: 1101px;
    height: 645px;
    border: 1px solid var(--trim);
    box-sizing: border-box;
  }
  .holder-name {
    position: absolute;
    left: 50px;
    top: 48px;
    margin: 0;
    font-family: "Arimo", Arial, sans-serif;
    font-weight: 400;
    font-size: 40px;
    line-height: 1;
    color: var(--name-blue);
  }
  .monogram {
    position: absolute;
    left: 60px;
    top: 150px;
    width: 460px;
    margin: 0;
    text-align: center;
    font-family: "Roboto Condensed", "Arial Narrow", sans-serif;
    font-weight: 700;
    font-size: 300px;
    line-height: 300px;
    color: var(--brand-blue);
  }
  .brand-band {
    position: absolute;
    left: 44px;
    top: 470px;
    width: 556px;
    height: 76px;
    display: flex;
    align-items: center;
    justify-content: center;
    gap: 16px;
  }
  .brand-square {
    width: 40px;
    height: 40px;
    background: var(--brand-green);
    flex: none;
  }
  .brand-name {
    font-family: "Roboto Condensed", "Arial Narrow", sans-serif;
    font-weight: 700;
    font-size: 66px;
    line-height: 1;
    color: var(--brand-blue);
    white-space: nowrap;
  }
  .holder-title {
    position: absolute;
    left: 44px;
    top: 549px;
    width: 556px;
    margin: 0;
    text-align: center;
    font-family: "Arimo", Arial, sans-serif;
    font-weight: 400;
    font-size: 21px;
    line-height: 24px;
    letter-spacing: 3.6px;
    color: var(--tagline);
    white-space: nowrap;
  }
  .divider {
    position: absolute;
    left: 642px;
    top: 205px;
    width: 2px;
    height: 367px;
    background: var(--rule);
  }
  .address {
    position: absolute;
    left: 658px;
    top: 206px;
    margin: 0;
    font-family: "Roboto Condensed", "Arial Narrow", sans-serif;
    font-style: normal;
    font-size: 37px;
    line-height: 47px;
    color: var(--ink);
  }
  .contact-list {
    position: absolute;
    left: 660px;
    top: 438px;
    margin: 0;
    padding: 0;
    list-style: none;
    font-family: "Roboto Condensed", "Arial Narrow", sans-serif;
    font-size: 37px;
    line-height: 47px;
    color: var(--ink);
  }
  .contact-item {
    display: flex;
    align-items: center;
    white-space: nowrap;
  }
  .contact-icon {
    width: 28px;
    height: 28px;
    flex: none;
    margin-right: 28px;
  }
  .contact-sep {
    margin-right: 8px;
  }
</style>
</head>
<body>
<main class="card">
  <div class="trim-line"></div>

  <h1 class="holder-name">Gareth Pennock</h1>

  <p class="monogram">kr</p>

  <div class="brand-band">
    <span class="brand-square"></span>
    <span class="brand-name">Korvanta Reach</span>
  </div>
  <p class="holder-title">INTERNET MARKETING STRATEGIST</p>

  <div class="divider"></div>

  <address class="address">
    No. 2156 N. Halvern Ave.,<br>
    Ste. 118 Tucson,<br>
    Arizona 85710
  </address>

  <ul class="contact-list">
    <li class="contact-item">
      <svg class="contact-icon" viewBox="0 0 28 28" aria-hidden="true">
        <path d="M9 4 L12 4 L12 10 L10 11 Q10 16 12 19 L12 24 L9 24 Q5 20 5 14 Q5 8 9 4 Z" fill="var(--ink)"/>
      </svg>
      <span class="contact-sep">:</span>(555) 813-2064
    </li>
    <li class="contact-item">
      <svg class="contact-icon" viewBox="0 0 28 28" aria-hidden="true">
        <rect x="2" y="6" width="24" height="16" fill="none" stroke="var(--ink)" stroke-width="1.4"/>
        <path d="M2 6 L14 16 L26 6 M2 22 L11 13 M26 22 L17 13" fill="none" stroke="var(--ink)" stroke-width="1.4"/>
      </svg>
      <span class="contact-sep">:</span>gareth@korvantareach.com
    </li>
    <li class="contact-item">
      <svg class="contact-icon" viewBox="0 0 28 28" aria-hidden="true">
        <circle cx="14" cy="14" r="11" fill="var(--ink)"/>
        <path d="M8 10 Q11 8 13 11 Q12 14 9 14 Z M15 17 Q19 15 21 18 Q19 22 16 21 Z" fill="var(--paper)"/>
      </svg>
      <span class="contact-sep">:</span>www.korvantareach.com
    </li>
  </ul>
</main>
</body>
</html>
```